business cards for a home design center

Easy to read Business CArd I am uploading the logo. you will see the color scheme we need.
Also after the design of the business card I need to be changing the employee name and cel phone. as needed.
I want to try those clear business cards and also not clear ones.
I want for business card to be transitional not too busy, and not that plain. hopw you can get my feeling.
I think the logo I attached will help you understand more the consept

Target Market(s)

Builders in town, people building home, office, commercial residential.

Industry/Entity Type

Home Improvement

Contact Information for Business Card

Marisol Quintero
Office-958-341-2265
Fax 958-341-2290
Cell 958-5204316
website. www.velmontinteriorhall.com
email marisol@velmontinteriorhall.com

Requirements
Must have
• Elegant, sleek,
Nice to have
• write on the back of the card like appointments or notes
Should not have
• Not all black

```html
<!DOCTYPE html>
<html lang="en">
<head>
<meta charset="utf-8">
<title>Velmont Interior Hall – Business Card</title>
<link rel="stylesheet" href="https://fonts.googleapis.com/css2?family=Arimo:wght@400;700&display=swap">
<style>
  :root {
    --ink: #231f20;
    --black: #0b0c0e;
    --gold-light: #f0cf63;
    --gold: #d3a63f;
    --gold-deep: #b8892f;
    --accent-yellow: #f2c21a;
    --rule: #8a8a8a;
    --edge: #6d6e71;
    --paper: #ffffff;
    --brand-grey: #3a3d42;
  }
  * { box-sizing: border-box; margin: 0; padding: 0; }
  html, body { width: 1200px; height: 1200px; overflow: hidden; background: var(--paper); }
  body { position: relative; font-family: "Arimo", "Helvetica Neue", Arial, sans-serif; color: var(--ink); }

  .card {
    position: absolute;
    left: 189px;
    width: 821px;
    height: 463px;
    border: 1px solid var(--edge);
    background: var(--paper);
    overflow: hidden;
  }
  .card--front { top: 118px; }
  .card--back { top: 618px; }

  .front__panel {
    position: absolute; left: 0; top: 0; bottom: 0; width: 362px;
    background: var(--black);
  }
  .front__frame {
    position: absolute; left: 25px; top: 26px; width: 770px; height: 410px;
    border: 6px solid transparent;
    border-image: linear-gradient(135deg, var(--gold-deep), var(--gold-light) 45%, var(--gold) 70%, var(--gold-light)) 1;
  }
  .front__brand {
    position: absolute; left: 40px; top: 150px; width: 302px;
    display: flex; align-items: center; justify-content: center; gap: 12px;
  }
  .front__brand-mark { width: 14px; height: 14px; background: var(--gold-light); flex: none; }
  .front__brand-name {
    font-weight: 700; font-size: 27px; line-height: 1.25; color: var(--gold-light);
    text-align: center; letter-spacing: 0.5px;
  }

  .contact { position: absolute; left: 385px; top: 150px; }
  .contact__name { font-weight: 700; font-size: 32px; line-height: 1; color: var(--ink); margin-bottom: 21px; }
  .contact__list { list-style: none; }
  .contact__item {
    display: flex; align-items: center; height: 31px;
    font-size: 24px; color: var(--ink);
  }
  .contact__icon { width: 24px; height: 24px; margin-right: 20px; flex: none; }

  .back__title {
    position: absolute; left: 53px; top: 74px;
    font-size: 26px; letter-spacing: 6.5px; color: var(--accent-yellow); font-weight: 400;
  }
  .back__brand {
    position: absolute; right: 52px; top: 44px; width: 120px;
    font-weight: 700; font-size: 17px; line-height: 1.2; text-align: center; color: var(--brand-grey);
  }
  .back__lines { position: absolute; left: 53px; top: 167px; width: 890px; list-style: none; }
  .back__line { height: 60px; border-top: 2px solid var(--rule); width: 712px; }
</style>
</head>
<body>
  <section class="card card--front" aria-label="Business card front">
    <div class="front__panel"></div>
    <div class="front__frame"></div>
    <div class="front__brand">
      <span class="front__brand-mark"></span>
      <span class="front__brand-name">Velmont<br>Interior Hall</span>
    </div>
    <div class="contact">
      <h1 class="contact__name">Marisol Quintero</h1>
      <ul class="contact__list">
        <li class="contact__item">
          <svg class="contact__icon" viewBox="0 0 24 24" aria-label="Office"><path fill="#d9ae3e" d="M2 11c0-4 20-4 20 0v2h-5v-2c-2-1-8-1-10 0v2H2z"/><ellipse cx="12" cy="16" rx="7" ry="5" fill="#e6bd4c"/><circle cx="12" cy="16" r="2.5" fill="#fff"/></svg>958-341-2265
        </li>
        <li class="contact__item">
          <svg class="contact__icon" viewBox="0 0 24 24" aria-label="Fax"><rect x="6" y="2" width="11" height="10" fill="#e6bd4c"/><rect x="3" y="12" width="18" height="9" fill="#d9ae3e"/><rect x="8" y="5" width="7" height="1.5" fill="#fff"/><rect x="8" y="8" width="7" height="1.5" fill="#fff"/></svg>958-341-2290
        </li>
        <li class="contact__item">
          <svg class="contact__icon" viewBox="0 0 24 24" aria-label="Cell"><rect x="6" y="1" width="12" height="22" rx="3" fill="#e6bd4c"/><rect x="8" y="4" width="8" height="14" fill="#fff"/></svg>958-5204316
        </li>
        <li class="contact__item">
          <svg class="contact__icon" viewBox="0 0 24 24" aria-label="Email"><rect x="1" y="5" width="22" height="15" fill="#e6bd4c"/><path d="M1 5l11 8 11-8" fill="none" stroke="#fff" stroke-width="1.5"/></svg>marisol@velmontinteriorhall.com
        </li>
        <li class="contact__item">
          <svg class="contact__icon" viewBox="0 0 24 24" aria-label="Website"><circle cx="12" cy="12" r="10" fill="#e6bd4c"/><g fill="none" stroke="#fff" stroke-width="1.3"><ellipse cx="12" cy="12" rx="4" ry="10"/><path d="M2 12h20M4 7h16M4 17h16"/></g></svg>www.vihsw.com
        </li>
      </ul>
    </div>
  </section>

  <section class="card card--back" aria-label="Business card back">
    <h2 class="back__title">APPOINTMENTS</h2>
    <div class="back__brand">Velmont<br>Interior Hall</div>
    <ul class="back__lines">
      <li class="back__line"></li>
      <li class="back__line"></li>
      <li class="back__line"></li>
      <li class="back__line"></li>
      <li class="back__line"></li>
    </ul>
  </section>
</body>
</html>
```